Startup online payment business - Sporting / Golf, Swift Tee payment

Background:
Our business name is "Swift Tee" we provide online payments for golfing services via our website. We currently have a logo used on our website. No other design style has been developed. Our aim is to remove cash payments for service at golf clubs.

Our Key Values:
Quick and easy
Formal and polite
Fun with professional boundary
Mate-ship relationships
100% online digital

What we want from you:
Marketing design to be used on posters and stickers in a retail setting to direct customers to our online payment Chanel.
Design must incorporate attached logo, URL swifttee.com.au and our key values can act as a guide the type of design. We have used color Hex#007672 for logo background. We are open to use other colors.

Target Market(s)

Golf clubs and golf players

Industry/Entity Type

Golf Course

Font styles to use
Sans Serif

Requirements
Must have
• Directions to online payment via URL: swifttee.com.au
Nice to have
• We like the idea of the slogan: No Cash - No worries. Have attached home screen that will be available from URL link. Consideration if using mobile phone in image. Push the online payment and steps 1. Visit swifttee.com 2. Select club 3. Confirm payment
Should not have
• Cartoons

```html
<!DOCTYPE html>
<html lang="en">
<head>
<meta charset="utf-8">
<title>Swift Tee – No Cash, No worries</title>
<link rel="stylesheet" href="https://fonts.googleapis.com/css2?family=Jost:wght@300;400;500;700&display=swap">
<style>
  :root {
    --brand-teal: #007672;
    --paper: #ffffff;
    --backdrop: #d4d4d6;
    --ink: #1a1a1a;
    --turf-light: #c9c46a;
    --turf-mid: #8f9a34;
    --turf-deep: #4f6320;
  }
  * { box-sizing: border-box; margin: 0; padding: 0; }
  html, body {
    width: 1200px; height: 1200px; overflow: hidden;
    background: var(--backdrop);
    font-family: "Jost", sans-serif;
  }
  .poster {
    position: absolute;
    left: 239px; top: 96px;
    width: 713px; height: 1007px;
    background: var(--paper);
  }
  .hero-photo {
    position: absolute;
    left: 0; top: 102px;
    width: 713px; height: 477px;
    background:
      linear-gradient(180deg, #e9efe0 0%, #6f8a3a 22%, var(--turf-light) 40%, var(--turf-mid) 70%, var(--turf-deep) 100%);
  }
  .brand-block {
    position: absolute;
    left: 31px; top: 31px;
    width: 202px; height: 161px;
    background: var(--brand-teal);
    display: flex; align-items: center; justify-content: center;
  }
  .brand-name {
    color: var(--paper);
    font-weight: 500;
    font-size: 36px;
    letter-spacing: 1px;
  }
  .headline {
    position: absolute;
    left: 0; top: 628px; width: 713px;
    text-align: center;
    color: var(--brand-teal);
    font-weight: 700;
    font-size: 60px;
    line-height: 1.1;
    letter-spacing: 0.5px;
  }
  .rule {
    position: absolute;
    left: 32px; width: 648px; height: 2px;
    background: var(--brand-teal);
  }
  .rule--top { top: 702px; }
  .rule--bottom { top: 835px; }
  .values {
    position: absolute;
    top: 716px;
    list-style: none;
    font-weight: 300;
    font-size: 25px;
    line-height: 36px;
    color: var(--ink);
  }
  .values--left { left: 34px; }
  .values--right { left: 336px; }
  .values li::before { content: "• "; font-weight: 500; }
  .url-badge {
    position: absolute;
    left: 313px; top: 915px;
    width: 369px; height: 62px;
    background: var(--brand-teal);
    display: flex; align-items: center; gap: 10px;
    padding-left: 24px;
    color: var(--paper);
    font-weight: 500;
    font-size: 25px;
  }
  .url-badge svg { flex: none; }
</style>
</head>
<body>
  <main class="poster">
    <div class="hero-photo" role="img" aria-label="Close-up photo of a putter about to strike a golf ball on sunlit grass, golfer's shoes either side"></div>

    <div class="brand-block">
      <span class="brand-name">Swift Tee</span>
    </div>

    <h1 class="headline">No Cash - No worries</h1>
    <div class="rule rule--top"></div>

    <ul class="values values--left">
      <li>Quick and easy</li>
      <li>Formal and polite</li>
    </ul>
    <ul class="values values--right">
      <li>Fun with professional boundary</li>
      <li>Mate-ship relationships</li>
      <li>100% online digital</li>
    </ul>

    <div class="rule rule--bottom"></div>

    <div class="url-badge">
      <svg width="34" height="34" viewBox="0 0 34 34" aria-hidden="true" fill="none" stroke="#ffffff" stroke-width="2">
        <circle cx="17" cy="17" r="15"/>
        <ellipse cx="17" cy="17" rx="7" ry="15"/>
        <line x1="17" y1="2" x2="17" y2="32"/>
        <line x1="2" y1="17" x2="32" y2="17"/>
        <path d="M5 9.5h24M5 24.5h24"/>
      </svg>
      <span class="url-text">https://swifttee.com.au/</span>
    </div>
  </main>
</body>
</html>
```